Etiketten für Honigwein
Zielgruppe
Wir sind eine kleine Metmanufaktur im Süden des Schwarzwalds und haben uns auf den Namen
Tarquil getauft. Bei unseren Produkten setzen wir auf Qualität statt auf Quantität. Zu unserer
Zielgruppe gehören exklusive Schlossrestaurants, Gaststätten in antikem oder mittelalterlichen
Ambiente sowie Mittelaltermärkte. Später soll diese auf Feinkostläden und auch den Getränkehandel
erweitert werden.
Aufgabenstellung
Siehe angehängtes PDF.
Falls ein Designer eine bessere Idee zu manchen Punkten oder dem gesamten Design hat, sind wir gerne bereit, uns von diesen inspirieren zu lassen.
Posivitbeispiele sind mit Positiv1, Positiv2, etc. und Negativbeispiele mit Negativ1, Negativ2, etc. beschriftet.

```html
<!DOCTYPE html>
<html lang="de">
<head>
<meta charset="utf-8">
<title>Tarquil – Schwarzwälder Met, Etikett Kirsch-Met</title>
<link rel="stylesheet" href="https://fonts.googleapis.com/css2?family=Josefin+Sans:wght@400;600&display=swap">
<style>
  :root {
    --bg-top: #2a2c31;
    --bg-mid: #36383e;
    --bg-bottom: #17181c;
    --silver: #e6e7e6;
    --silver-dim: #c9cac9;
    --label-black: #0b0b0c;
    --label-edge: #2b2b2e;
    --forest: #7a2a45;
    --forest-deep: #4e1a2e;
    --cherry: #d9625f;
    --cherry-light: #e79a98;
    --kirsch-red: #e2675f;
    --cap-red: #a8282a;
  }
  * { margin: 0; padding: 0; box-sizing: border-box; }
  html, body { width: 1200px; height: 900px; overflow: hidden; }
  body {
    position: relative;
    background: radial-gradient(ellipse at 50% 48%, var(--bg-mid) 0%, var(--bg-top) 40%, var(--bg-bottom) 85%);
    font-family: "Josefin Sans", "Helvetica Neue", Arial, sans-serif;
    color: var(--silver);
  }

  /* Brand header */
  .brand {
    position: absolute;
    top: 70px;
    left: 200px;
    width: 800px;
    text-align: center;
  }
  .brand__name {
    font-weight: 600;
    font-size: 118px;
    letter-spacing: 0.08em;
    line-height: 1;
    color: var(--silver);
  }
  .brand__rule {
    height: 4px;
    background: var(--silver-dim);
    margin: 14px 0 12px;
  }
  .brand__tagline {
    text-align: right;
    font-size: 30px;
    letter-spacing: 0.32em;
    color: var(--silver-dim);
  }

  /* Main label, flat */
  .label {
    position: absolute;
    top: 300px;
    left: 380px;
    width: 440px;
    height: 560px;
    background: var(--label-black);
    border: 1px solid var(--label-edge);
    overflow: hidden;
  }
  .label__brand {
    position: absolute;
    top: 34px;
    left: 0;
    width: 100%;
    text-align: center;
  }
  .label__name {
    font-weight: 600;
    font-size: 56px;
    letter-spacing: 0.08em;
    color: var(--silver);
    line-height: 1;
  }
  .label__tagline {
    margin-top: 8px;
    font-size: 15px;
    letter-spacing: 0.2em;
    color: var(--silver-dim);
  }
  .label__illustration {
    position: absolute;
    top: 140px;
    left: 95px;
    width: 250px;
    height: 200px;
    border-radius: 8px;
    background: radial-gradient(circle at 42% 55%, var(--cherry-light) 0%, var(--cherry) 30%, #3a2022 68%, var(--label-black) 100%);
  }
  .label__variety {
    position: absolute;
    top: 360px;
    width: 100%;
    text-align: center;
    font-size: 22px;
    letter-spacing: 0.06em;
    color: var(--kirsch-red);
  }
  .label__type {
    position: absolute;
    top: 398px;
    width: 100%;
    text-align: center;
    font-size: 20px;
    letter-spacing: 0.06em;
    line-height: 1.15;
    color: var(--silver);
  }
  .label__forest {
    position: absolute;
    left: 0;
    bottom: 0;
    width: 100%;
    height: 88px;
    background: linear-gradient(to bottom, var(--label-black) 0%, var(--forest-deep) 45%, var(--forest) 100%);
  }

  /* Neck label, flat */
  .neck-label {
    position: absolute;
    top: 300px;
    left: 860px;
    width: 110px;
    height: 190px;
    background: var(--label-black);
    border: 1px solid var(--label-edge);
    border-top: 14px solid var(--cap-red);
    display: flex;
    align-items: center;
    justify-content: center;
  }
  .neck-label__variety {
    writing-mode: vertical-rl;
    font-size: 15px;
    letter-spacing: 0.08em;
    color: var(--kirsch-red);
  }
</style>
</head>
<body>
  <header class="brand">
    <div class="brand__name">TARQUIL</div>
    <div class="brand__rule"></div>
    <div class="brand__tagline">SCHWARZWÄLDER MET</div>
  </header>

  <section class="label">
    <div class="label__brand">
      <div class="label__name">TARQUIL</div>
      <div class="label__tagline">SCHWARZWÄLDER MET</div>
    </div>
    <div class="label__illustration" role="img" aria-label="Linienzeichnung zweier roter Kirschen mit Stielen neben einem Glas und einem Honigglas"></div>
    <div class="label__variety">KIRSCH-MET</div>
    <div class="label__type">HONIGWEIN<br>2022</div>
    <div class="label__forest" role="img" aria-label="Silhouette eines Tannenwaldes in Weinrot"></div>
  </section>

  <aside class="neck-label">
    <span class="neck-label__variety">KIRSCH-MET</span>
  </aside>
</body>
</html>
```